Social Media Graphics - Copperfield Loop

Create 6-7 individual social media graphics (square size) to encourage folks to join our online course, using either of the text below (only one set of text per graphic:

The Lantern Ridge Method
How to Create a 7-Figure Business From Scratch
Sign Up Today!

Or

The Lantern Ridge Method
Fast-track Your Way to a Multi-Million Business!
Sign Up Today!

For the color scheme of the graphics, use 1 or 2 colors in the color palette attached; or use any colors that look nice with their outfits; AVOID using red, white and blue altogether because it will look like an Independence Day (4th of July) graphic and we don’t want that; make sure the graphics appeal to both men and women

Make sure each graphic contains 1 of the 2 pics attached; and make sure one of the graphics is all TEXT only.

Target Market(s)

men and women looking to make more money

Industry/Entity Type

entrepreneurship

Requirements
Must have
• see the text document attached
Nice to have
• We are open to a nice color design; the color palette colors are not required, especially we don't want red, white and blue used together
Should not have
• AVOID using red, white and blue altogether because it will look like an Independence Day (4th of July) graphic and we dont want that

```html
<!DOCTYPE html>
<html lang="en">
<head>
<meta charset="utf-8">
<title>The Lantern Ridge Method – Social Graphics</title>
<link href="https://fonts.googleapis.com/css2?family=Anton&family=Poppins:wght@600&family=Roboto:wght@700&display=swap" rel="stylesheet">
<style>
  :root {
    --board: #888888;
    --blush: #f6d0d6;
    --blush-soft: #fcdcdc;
    --blush-light: #fbe9ea;
    --crimson: #b5121b;
    --crimson-deep: #9e111c;
    --scarlet: #ee2a3c;
    --fire: #f31c24;
    --fire-light: #ff4646;
    --signal: #d0112b;
    --espresso: #1c1416;
    --ink: #22181a;
    --cream: #fff6ef;
    --tint: #fde3e5;
    --photo-a: #3a2a2a;
    --photo-b: #c98a7a;
  }
  * { margin: 0; padding: 0; box-sizing: border-box; }
  html, body { width: 1200px; height: 729px; overflow: hidden; background: var(--board); }
  .board { position: relative; width: 1200px; height: 729px; }
  .tile { position: absolute; width: 278px; height: 278px; overflow: hidden; }
  .tile > * { position: absolute; }
  .display { font-family: "Anton", "Impact", sans-serif; font-weight: 400; line-height: 1.08; }
  .body-sans { font-family: "Poppins", "Arial", sans-serif; font-weight: 600; }
  .strong-sans { font-family: "Roboto", "Arial", sans-serif; font-weight: 700; }
  .photo { background: linear-gradient(135deg, var(--photo-a), var(--photo-b)); }

  /* Tile 1 */
  .tile--blush { left: 136px; top: 86px; background: var(--blush); }
  .tile--blush .title { top: 14px; left: 0; width: 100%; text-align: center; font-size: 20px; color: var(--crimson); }
  .tile--blush .subtitle { top: 57px; left: 0; width: 100%; text-align: center; font-size: 22px; line-height: 24px; color: var(--crimson-deep); }
  .tile--blush .ring { left: 12px; top: 123px; width: 254px; height: 254px; border-radius: 50%; background: var(--blush-light); border: 3px solid #f5a9b4; }
  .tile--blush .photo { left: 26px; top: 140px; width: 186px; height: 138px; border-radius: 90px 90px 0 0; }
  .tile--blush .badge { left: 178px; top: 140px; width: 100px; height: 100px; border-radius: 50%; background: var(--signal); display: flex; align-items: center; justify-content: center; text-align: center; color: var(--cream); font-size: 17px; line-height: 1.35; }
  .tile--blush .badge::after { content: ""; position: absolute; inset: 4px; border-radius: 50%; border: 1px solid rgba(255,246,239,.7); }

  /* Tile 2 */
  .tile--scarlet { left: 448px; top: 86px; background: var(--scarlet); }
  .tile--scarlet .title { top: 18px; right: 19px; text-align: right; font-size: 22px; color: var(--cream); }
  .tile--scarlet .subtitle { top: 86px; right: 22px; text-align: right; font-size: 16px; line-height: 21.5px; color: var(--tint); }
  .tile--scarlet .photo { left: -20px; top: 45px; width: 180px; height: 180px; border-radius: 50%; border: 3px solid var(--cream); }
  .tile--scarlet .cta { top: 229px; right: 19px; font-size: 27px; color: var(--cream); }

  /* Tile 3 */
  .tile--fire { left: 759px; top: 86px; background: var(--cream); }
  .tile--fire .field { left: 0; top: 0; width: 278px; height: 237px; background: radial-gradient(circle at 80% 20%, var(--fire-light), var(--fire) 60%); }
  .tile--fire .title { top: 10px; left: 0; width: 100%; text-align: center; font-size: 38px; line-height: 1.2; color: var(--cream); }
  .tile--fire .subtitle { top: 118px; left: 0; width: 100%; text-align: center; font-size: 19px; line-height: 25px; color: var(--cream); }
  .tile--fire .cta { top: 241px; left: 0; width: 100%; text-align: center; font-size: 24px; color: var(--signal); }

  /* Tile 4 */
  .tile--rose { left: 136px; top: 399px; background: var(--blush-soft); }
  .tile--rose .glow { left: -60px; top: -120px; width: 210px; height: 210px; border-radius: 50%; background: #f8c2c2; }
  .tile--rose .photo { left: 0; top: 24px; width: 164px; height: 191px; border-radius: 80px 0 0 0; }
  .tile--rose .title { top: 11px; left: 170px; font-size: 18px; color: var(--ink); }
  .tile--rose .subtitle { top: 70px; left: 170px; font-size: 17px; line-height: 23.5px; color: var(--ink); }
  .tile--rose .band { left: 0; top: 215px; width: 278px; height: 63px; background: var(--espresso); display: flex; align-items: center; justify-content: center; font-size: 26px; color: var(--cream); }

  /* Tile 5 */
  .tile--dark { left: 448px; top: 399px; background: var(--espresso); }
  .tile--dark .title { top: 20px; left: 12px; font-size: 24px; color: var(--cream); }
  .tile--dark .subtitle { top: 88px; left: 12px; font-size: 16px; line-height: 21.5px; color: var(--cream); }
  .tile--dark .photo { left: 123px; top: 49px; width: 180px; height: 180px; border-radius: 50%; border: 3px solid var(--scarlet); }
  .tile--dark .cta { top: 232px; left: 12px; font-size: 27px; color: var(--cream); }

  /* Tile 6 */
  .tile--text { left: 759px; top: 399px; background: var(--blush-soft); }
  .tile--text .bubble-a { left: -50px; top: 40px; width: 150px; height: 150px; border-radius: 50%; background: var(--blush-light); opacity: .7; }
  .tile--text .bubble-b { left: 140px; top: 120px; width: 180px; height: 180px; border-radius: 50%; background: var(--blush-light); opacity: .7; }
  .tile--text .band-top { left: 0; top: 0; width: 278px; height: 52px; background: var(--espresso); display: flex; align-items: center; justify-content: center; font-size: 22px; color: var(--cream); }
  .tile--text .message { top: 70px; left: 0; width: 100%; text-align: center; font-size: 30px; line-height: 36.5px; color: #e3141d; }
  .tile--text .band-bottom { left: 0; top: 233px; width: 278px; height: 45px; background: var(--espresso); display: flex; align-items: center; justify-content: center; font-size: 22px; color: var(--cream); }
</style>
</head>
<body>
<main class="board">

  <section class="tile tile--blush">
    <h2 class="title display">THE LANTERN RIDGE METHOD</h2>
    <p class="subtitle strong-sans">How to Create a<br>7-Figure Business<br>From Scratch</p>
    <div class="ring"></div>
    <div class="photo" role="img" aria-label="Photo of the two course hosts standing with arms crossed"></div>
    <div class="badge display">Sign Up<br>Today</div>
  </section>

  <section class="tile tile--scarlet">
    <div class="photo" role="img" aria-label="Circular photo of the two course hosts smiling"></div>
    <h2 class="title display">The Lantern<br>Ridge Method</h2>
    <p class="subtitle body-sans">How to<br>Create a<br>7-Figure<br>Business<br>From<br>Scratch</p>
    <p class="cta display">Sign Up Today!</p>
  </section>

  <section class="tile tile--fire">
    <div class="field"></div>
    <h2 class="title display">The Lantern<br>Ridge Method</h2>
    <p class="subtitle body-sans">How to Create<br>a 7-Figure<br>Business From<br>Scratch</p>
    <p class="cta display">Sign Up Today!</p>
  </section>

  <section class="tile tile--rose">
    <div class="glow"></div>
    <div class="photo" role="img" aria-label="Photo of the two course hosts standing side by side"></div>
    <h2 class="title display">The Lantern<br>Ridge Method</h2>
    <p class="subtitle body-sans">How to<br>Create<br>a 7-Figure<br>Business<br>From<br>Scratch</p>
    <p class="band display">Sign Up Today</p>
  </section>

  <section class="tile tile--dark">
    <h2 class="title display">The Lantern<br>Ridge Method</h2>
    <p class="subtitle body-sans">How to<br>Create a<br>7-Figure<br>Business<br>From<br>Scratch</p>
    <div class="photo" role="img" aria-label="Circular photo of the two course hosts smiling"></div>
    <p class="cta display">Sign Up Today!</p>
  </section>

  <section class="tile tile--text">
    <div class="bubble-a"></div>
    <div class="bubble-b"></div>
    <h2 class="band-top display">The Lantern Ridge Method</h2>
    <p class="message strong-sans">Fast-track Your<br>Way to a<br>Multi-Million<br>Business!</p>
    <p class="band-bottom display">Sign Up Today!</p>
  </section>

</main>
</body>
</html>
```